Affiliate website design and wireframe

We need a design of an affiliate website for an application we purchased, it is important that you build the website pages according to the developer of the applications specifications (please see attached documents) the developer of the application will configure the pages and add them to the site. Please take special note of his comments below.

We all so need you to create a wire frame so the developer can test everything (http://sketchwire.tolvaro.vn/)

It will be the homepage and about 16 inner pages (please see attached files)
Here is our website http://bluvendmarket.com/affiliate/affiliates/index.php

The version of the software we purchased is the Kivo Partner Hubline version

Comments from the developers

1. I will need the source files of the design (photoshop .psd files and font files if custom fonts are used), since the implementation is closely bound to component sizes (like border width, margin width etc.) and colors. If you own a corporate design manual, it's crucial to send it as well. Also, please, make sure if you use custom fonts, that these allow legal website integration (like google web fonts).

2. Any and every content is controlled via templates. All editing/adding/removing etc. is done here. The template files are essentially html/php documents, they use a template engine called quillo (http://www.quillo.net/) which has it's own language similar to php.

3. .psd files are ideal, because we deal with the specifics of KPX/KPH implementation on a daily basis. Any html/css developed in advance may prove to be a poor choice. You may choose to let an in-house developer do the job, but experience wise this is more costly, since he will not be accustomed to the template/functionality systems of KPX/KPH.

4. I will need the source files of the design (photoshop .psd files and font files if custom fonts are used), since the implementation is closely bound to component sizes (like border width, margin width etc.) and colors. If you own a corporate design manual, it's crucial to send it as well. Also, please, make sure if you use custom fonts, that these allow legal website integration (like google web fonts).

Regards,

Dorek Hanval
Multimedia Design

We prefer illustrations more than pictures of real people.

This is the home page, it is asking for Merchant and Affiliate sign up, not just affiliate.

http://bluvendmarket.com/affiliate/index.php

Please note the home page features both Merchant and Affiliate sign up

We are looking for illustration design not just stock images

Please remember the search menu that searches for the available programs, see the example we gave you, look at the search menu at the top of the page http://www.tradelumo.com/

We are reviewing everything, no need to send more designs

Target Market(s)

Natural Products Manufacturers
Natural products Sales reps
Natural Products Bloggers
Social Marketing

Industry/Entity Type

Software

Requirements
Must have
• 1. All links on pages should go to the appropriate pages.
2. Colors can be based on our logo design (look at the attachments)
3. Here is our website http://bluvendmarket.com/affiliate/affiliates/index.php
4. We have attached a drawing of how we think the homepage concept should follow.
5. Main concept of design, is trying to show our sales people (Affiliates) are doing multiple things to advertise and sell the merchants products.(see logo)
6. Need to be able to edit all text and images.
7. Our target audience is Natural product sales people (Advertisers, bloggers, ext) and natural product manufacturers.
8. You can speak to the company who made the application, through live chat, on there website http://www.kivopartnerhubline.com/
Nice to have
• See Attached Documents.
site should take up whole website pages
Look For fun Illustrated Website, one of the better ones we have seen is http://www.tradelumo.com/index.cfm
Should not have
• Please look very carefully at developers comment above.

```html
<!DOCTYPE html>
<html lang="en">
<head>
<meta charset="utf-8">
<title>Bluvend Market – Affiliate Marketing Network</title>
<link rel="stylesheet" href="https://fonts.googleapis.com/css2?family=Mulish:wght@400;700;800&family=Open+Sans:wght@400;600&family=Questrial&display=swap">
<style>
:root{
  --navy:#0c2d55;
  --heading:#0f3a6b;
  --teal:#1a97a6;
  --teal-dark:#12808f;
  --header-bg:#f0f1f1;
  --green:#a5d84a;
  --green-btn:#6bb81c;
  --green-btn-dark:#4f9a0e;
  --yellow:#f5d020;
  --text:#555a5f;
  --title-blue:#1a8fc9;
  --grey-section:#e9eaeb;
  --white:#ffffff;
}
*{box-sizing:border-box;margin:0;padding:0}
html,body{width:1051px;height:1200px;overflow:hidden;background:var(--white)}
body{position:relative;font-family:"Open Sans",sans-serif;color:var(--text)}
a{color:inherit;text-decoration:none}

.top-bar{position:absolute;left:0;top:0;width:1051px;height:32px;background:var(--navy)}
.top-links{position:absolute;left:97px;top:9px;font-size:11px;color:var(--white)}
.top-links span{margin:0 8px}
.login{position:absolute;top:0;height:31px;line-height:31px;text-align:center;font-size:12px;color:#1d2b10}
.login-affiliate{left:717px;width:119px;background:var(--green)}
.login-merchant{left:840px;width:124px;background:var(--yellow)}

.site-header{position:absolute;left:0;top:32px;width:1051px;height:151px;background:var(--header-bg)}
.brand{position:absolute;left:99px;top:88px;display:flex;align-items:center;gap:10px}
.brand-mark{width:34px;height:34px;border-radius:50%;background:var(--green-btn)}
.brand-name{font-family:"Mulish",sans-serif;font-weight:800;font-size:25px;color:var(--green-btn-dark);letter-spacing:-.5px}
.main-nav{position:absolute;top:102px;left:508px;display:flex;gap:38px;font-family:"Questrial",sans-serif;font-size:15px;color:#2b2b2b;white-space:nowrap}
.main-nav a{padding-bottom:9px;border-bottom:3px solid transparent}
.main-nav a.active{border-bottom-color:var(--green-btn)}

.hero-band{position:absolute;left:0;top:183px;width:1051px;height:318px;background:linear-gradient(180deg,var(--teal-dark),var(--teal))}
.hero-card{position:absolute;left:99px;top:199px;width:854px;height:354px;background:linear-gradient(90deg,#f6f6f6,#ffffff 55%);box-shadow:0 22px 24px -16px rgba(0,0,0,.45)}
.hero-art{position:absolute;left:481px;top:0;width:373px;height:354px;background:linear-gradient(135deg,#eef2f6 0%,#cfe0f2 45%,#e56aa4 75%,#3f8ad6 100%)}
.hero-title{position:absolute;z-index:1;left:34px;top:86px;font-family:"Mulish",sans-serif;font-weight:800;font-size:28px;color:var(--heading);letter-spacing:-.4px;white-space:nowrap}
.hero-text{position:absolute;left:36px;top:132px;width:400px;font-family:"Questrial",sans-serif;font-size:16px;line-height:21px;color:#333}
.hero-button{position:absolute;left:37px;top:229px;height:50px;display:flex}
.hero-button .label{width:219px;background:linear-gradient(180deg,var(--green-btn),var(--green-btn-dark));color:var(--white);font-family:"Mulish",sans-serif;font-weight:800;font-size:20px;line-height:50px;text-align:center}
.hero-button .arrow{width:46px;margin-left:2px;background:linear-gradient(180deg,var(--green-btn),var(--green-btn-dark));display:flex;align-items:center;justify-content:center}

.slider-dots{position:absolute;top:589px;left:482px;display:flex;gap:5px}
.slider-dots span{width:14px;height:14px;border-radius:50%;background:#6c6c6c}
.slider-dots span.current{background:#9a9a9a;box-shadow:inset 0 0 0 3px #6c6c6c}

.intro-title{position:absolute;top:632px;left:0;width:1051px;text-align:center;font-family:"Mulish",sans-serif;font-weight:800;font-size:20px;color:var(--heading);white-space:nowrap}
.intro-text{position:absolute;top:670px;left:80px;width:891px;text-align:center;font-size:13.6px;line-height:19.5px;color:var(--text);letter-spacing:-.1px}
.tools-title{position:absolute;top:770px;left:0;width:1051px;text-align:center;font-family:"Mulish",sans-serif;font-weight:800;font-size:19.5px;color:var(--heading)}

.tools{position:absolute;left:0;top:815px;width:1051px;height:359px;background:var(--grey-section)}
.tools::before{content:"";position:absolute;left:290px;top:0;width:470px;height:8px;background:radial-gradient(ellipse at top,rgba(0,0,0,.22),transparent 70%)}
.tool{position:absolute;width:380px;height:100px}
.tool-icon{position:absolute;left:0;top:0;width:86px;height:86px;border-radius:50%;display:flex;align-items:center;justify-content:center}
.tool-title{position:absolute;left:100px;top:0;font-family:"Mulish",sans-serif;font-weight:700;font-size:16.5px;color:var(--title-blue);white-space:nowrap}
.tool-text{position:absolute;left:100px;top:25px;font-size:13px;line-height:19.5px;color:var(--text);white-space:nowrap}
.tool-more{position:absolute;left:100px;top:66px;font-size:12px;color:#111;text-decoration:underline}
.tool-links{left:99px;top:60px}
.tool-coupons{left:580px;top:60px}
.tool-banners{left:99px;top:231px}
.tool-video{left:580px;top:231px}
.icon-green{background:#a9d25b}
.icon-blue{background:#1eb4ea}
.icon-red{background:#e8184e}
.icon-yellow{background:#f8d40c}
.bottom-rule{position:absolute;left:190px;top:1178px;width:670px;height:1px;background:#d8d8d8}
</style>
</head>
<body>

<div class="top-bar">
  <nav class="top-links"><a href="#">HOME</a><span>|</span><a href="#">SIGN UP</a><span>|</span><a href="#">CONTACT US</a></nav>
  <a class="login login-affiliate" href="#">AFFILIATE LOGIN</a>
  <a class="login login-merchant" href="#">MERCHANT LOGIN</a>
</div>

<header class="site-header">
  <a class="brand" href="#"><span class="brand-mark"></span><span class="brand-name">BLUVEND MARKET</span></a>
  <nav class="main-nav">
    <a class="active" href="#">HOW IT WORKS</a>
    <a href="#">AFFFILAITE SIGNUP</a>
    <a href="#">MERCHANTS SIGN UP</a>
  </nav>
</header>

<div class="hero-band"></div>
<section class="hero-card">
  <div class="hero-art" role="img" aria-label="Illustration of a rising earnings arrow over a blue bar chart with a pink piggy bank"></div>
  <h1 class="hero-title">START MAKING MONEY NOW!</h1>
  <p class="hero-text">There is no charge to join our Affiliate Program. We pay commissions for all sales you referred.Earn up to 30% commissions</p>
  <a class="hero-button" href="#">
    <span class="label">AFFILIATES SIGNUP</span>
    <span class="arrow"><svg width="24" height="24" viewBox="0 0 24 24"><circle cx="12" cy="12" r="10" fill="none" stroke="#fff" stroke-width="2"/><path d="M7 12h9M12 8l4 4-4 4" fill="none" stroke="#fff" stroke-width="2"/></svg></span>
  </a>
</section>

<div class="slider-dots"><span class="current"></span><span></span><span></span><span></span><span></span></div>

<h2 class="intro-title">WE BUILD TOOLS TO HELP OUR CLIENTS SUCCEED IN AFFILIATE MARKETING</h2>
<p class="intro-text">Bluvend Market has been in business for 14 years, exclusively as an Affiliate Marketing Network. Our technology receives accolades for speed, efficiency, and accuracy – and our reputation as a fair and honest business is well known within the industry. We encourage you to browse around our website and learn more, but if you have any questions, please don't hesitate to contact us!</p>

<h2 class="tools-title">TOOLS - START TO LEARNING</h2>

<section class="tools">
  <article class="tool tool-links">
    <div class="tool-icon icon-green"><svg width="46" height="40" viewBox="0 0 46 40"><path d="M2 6h14l4 5h24v27H2z" fill="#1f2a1a"/><path d="M18 26l8-8" stroke="#a9d25b" stroke-width="3"/><rect x="13" y="22" width="9" height="6" rx="3" fill="none" stroke="#a9d25b" stroke-width="2" transform="rotate(-45 17 25)"/><rect x="23" y="15" width="9" height="6" rx="3" fill="none" stroke="#a9d25b" stroke-width="2" transform="rotate(-45 27 18)"/></svg></div>
    <h3 class="tool-title">PRODUCT LINKS</h3>
    <p class="tool-text">Promote specific products of your choosing by<br>utilizing our deep-linking tool, or get even ......</p>
    <a class="tool-more" href="#">Read More</a>
  </article>
  <article class="tool tool-coupons">
    <div class="tool-icon icon-blue"><svg width="42" height="42" viewBox="0 0 42 42"><rect x="8" y="4" width="28" height="32" fill="#f5a623"/><text x="22" y="27" text-anchor="middle" font-family="Mulish,sans-serif" font-weight="800" font-size="18" fill="#fff">%</text><circle cx="12" cy="37" r="4" fill="#d0202a"/><circle cx="22" cy="37" r="4" fill="#d0202a"/></svg></div>
    <h3 class="tool-title">COUPON &amp; DEALS</h3>
    <p class="tool-text">Provide your visitors with coupons or deals<br>supplied directly by merchant partners.</p>
    <a class="tool-more" href="#">Read More</a>
  </article>
  <article class="tool tool-banners">
    <div class="tool-icon icon-red"><svg width="44" height="40" viewBox="0 0 44 40"><rect x="4" y="4" width="36" height="24" fill="#9aa3ab" stroke="#333" stroke-width="2"/><path d="M16 28v10M28 28v10" stroke="#333" stroke-width="3"/></svg></div>
    <h3 class="tool-title">BANNERS &amp; TEXT LINKS</h3>
    <p class="tool-text">Incorporate banner ads on your sidebar or add<br>promotional affiliate links within blog posts.</p>
    <a class="tool-more" href="#">Read More</a>
  </article>
  <article class="tool tool-video">
    <div class="tool-icon icon-yellow"><svg width="44" height="40" viewBox="0 0 44 40"><path d="M4 8l34-6 1 6-34 6z" fill="#222"/><rect x="4" y="14" width="36" height="22" fill="#1f5fb0" stroke="#222" stroke-width="2"/><path d="M18 19l9 6-9 6z" fill="#fff"/></svg></div>
    <h3 class="tool-title">VIDEO CREATIVES</h3>
    <p class="tool-text">Add engaging how-to or promotional videos<br>to your site, supplied by merchant partners ...</p>
    <a class="tool-more" href="#">Read More</a>
  </article>
</section>
<div class="bottom-rule"></div>

</body>
</html>
```